Experienced Handyman needs a business card design

Need a business card design for a one-person Handyman business. This will be my second job (part-time) after retiring from a hands-on 30-year career. I'm experienced, a hard worker, friendly, and do quality work. Everybody needs a handman they can rely on! I've worked with wood and home renovations for 20 years on the side. I'm interested in small, quick jobs - not big renovations, or building decks or garages - more like home maintenance, installing sinks, - things like that.
Walter The Fixer LLC
Small Jobs Done Right
I'm wondering if the P or H could be made out of tools in my logo...?
Target Market(s)
Homeowners - small jobs
Industry/Entity Type
Handyman / Construction
Contact Information for Business Card
Business name & tagline (see description)...email (Walter@WalterTheFixerpro.example)...phone (555) 417-8862
Look and feel

```html
<!DOCTYPE html>
<html lang="en">
<head>
<meta charset="utf-8">
<title>Walter The Fixer – Business Cards</title>
<link rel="stylesheet" href="https://fonts.googleapis.com/css2?family=Archivo:wght@700;800&family=Michroma&display=swap">
<style>
  :root {
    --backdrop: #a0a1a3;
    --card-white: #ffffff;
    --brand-blue: #0f69ab;
    --brand-blue-deep: #0b5a98;
    --brand-blue-light: #1b78bd;
    --brand-yellow: #f2a900;
    --text-light: #ffffff;
  }
  html, body {
    margin: 0;
    padding: 0;
    width: 1200px;
    height: 900px;
    overflow: hidden;
    background: var(--backdrop);
  }
  .canvas {
    position: relative;
    width: 1200px;
    height: 900px;
  }
  .card {
    position: absolute;
    left: 325px;
    width: 550px;
    height: 313px;
    box-sizing: border-box;
    text-align: center;
    box-shadow: 0 4px 8px rgba(0, 0, 0, 0.35);
  }
  .card--front {
    top: 99px;
    background: var(--card-white);
  }
  .card--back {
    top: 488px;
    background: linear-gradient(90deg, var(--brand-blue-deep) 0%, var(--brand-blue-light) 50%, var(--brand-blue-deep) 100%);
  }
  .brand-mark {
    position: absolute;
    left: 50%;
    width: 100px;
    height: 100px;
    margin-left: -50px;
    background: var(--brand-yellow);
  }
  .card--front .brand-mark { top: 40px; }
  .card--back .brand-mark { top: 68px; }
  .brand {
    position: absolute;
    left: 0;
    right: 0;
  }
  .card--front .brand { top: 152px; }
  .card--back .brand { top: 180px; }
  .brand-name {
    font-family: "Archivo", sans-serif;
    font-weight: 800;
    font-size: 31px;
    letter-spacing: 0.3px;
    line-height: 1;
    text-transform: uppercase;
    color: var(--brand-blue);
  }
  .card--back .brand-name { color: var(--text-light); }
  .tagline {
    margin-top: 6px;
    font-family: "Michroma", sans-serif;
    font-size: 11.5px;
    letter-spacing: 0.6px;
    color: var(--brand-yellow);
  }
  .contact {
    position: absolute;
    left: 0;
    right: 0;
    top: 229px;
  }
  .contact-line {
    display: flex;
    justify-content: center;
    align-items: center;
    gap: 7px;
    color: var(--brand-blue);
  }
  .contact-phone {
    font-family: "Michroma", sans-serif;
    font-size: 19px;
    font-weight: 700;
    letter-spacing: 1.5px;
    -webkit-text-stroke: 0.6px var(--brand-blue);
  }
  .contact-email {
    margin-top: 10px;
    font-family: "Archivo", sans-serif;
    font-weight: 700;
    font-size: 17px;
  }
  .contact-line svg { fill: var(--brand-blue); }
  .website {
    position: absolute;
    left: 0;
    right: 0;
    top: 271px;
    font-family: "Archivo", sans-serif;
    font-weight: 700;
    font-size: 14px;
    letter-spacing: 0.5px;
    color: var(--text-light);
  }
</style>
</head>
<body>
<main class="canvas">
  <section class="card card--front" aria-label="Business card front">
    <div class="brand-mark" role="img" aria-label="Brand mark area"></div>
    <div class="brand">
      <div class="brand-name">Walter The Fixer</div>
      <div class="tagline">Small Jobs Done Right</div>
    </div>
    <div class="contact">
      <div class="contact-line contact-phone">
        <svg width="19" height="19" viewBox="0 0 24 24" aria-hidden="true"><path d="M6.6 10.8a15.1 15.1 0 0 0 6.6 6.6l2.2-2.2c.3-.3.7-.4 1-.2 1.1.4 2.3.6 3.6.6.6 0 1 .4 1 1V20c0 .6-.4 1-1 1A17 17 0 0 1 3 4c0-.6.4-1 1-1h3.5c.6 0 1 .4 1 1 0 1.3.2 2.5.6 3.6.1.3 0 .7-.2 1z"/></svg>
        <span>(555) 417-8862</span>
      </div>
      <div class="contact-line contact-email">
        <svg width="20" height="14" viewBox="0 0 20 14" aria-hidden="true"><path d="M0 0h20v14H0z"/><path d="M1.5 1.5 10 8l8.5-6.5" fill="none" stroke="#fff" stroke-width="1.4"/></svg>
        <span>Walter@WalterTheFixerpro.example</span>
      </div>
    </div>
  </section>

  <section class="card card--back" aria-label="Business card back">
    <div class="brand-mark" role="img" aria-label="Brand mark area"></div>
    <div class="brand">
      <div class="brand-name">Walter The Fixer</div>
      <div class="tagline">Small Jobs Done Right</div>
    </div>
    <div class="website">www.WalterTheFixerpro.example</div>
  </section>
</main>
</body>
</html>
```